Webdesign für Malerbetrieb
Zielgruppe
Malerbetrieb
Zielgruppe: private Haushalte, Wohnungsverwaltungen
Aufgabenstellung
Das Logo bitte integrieren.
Die Seite darf auf meine potentielle Kunden freundlich und einladend wirken. Die Grundfarben des Logos sollen bitte dezent vertreten werden, die Farbharmonie dabei sollte stimmen.
Da ich kein eigenes Bildmaterial habe, sind natürlich themabezogene Stock-Bilder erwünscht, aber wenn möglich bitte ohne Personen und die Seite nicht mit großen XXL-Bildern überladen.
Ansonsten lasse ich mich gerne von eurer Kreativität überraschen!

```html
<!DOCTYPE html>
<html lang="de">
<head>
<meta charset="utf-8">
<title>Lutz Malereibetrieb – Startseite</title>
<link rel="stylesheet" href="https://fonts.googleapis.com/css2?family=Montserrat:wght@300;400;500;700;800&display=swap">
<style>
  :root {
    --page-bg: #000000;
    --text-light: #ffffff;
    --text-muted: #cfcfcf;
    --accent-cyan: #1fb6ea;
    --accent-yellow: #f5e400;
    --accent-magenta: #e4168f;
    --photo-deep: #0b0b0d;
    --photo-mid: #2c2e33;
    --photo-warm: #6a5127;
    --photo-cool: #1d4a63;
  }
  * { margin: 0; padding: 0; box-sizing: border-box; }
  html, body {
    width: 1200px;
    height: 800px;
    overflow: hidden;
    background: var(--page-bg);
    font-family: "Montserrat", sans-serif;
    color: var(--text-light);
  }
  .hero {
    position: relative;
    width: 1200px;
    height: 800px;
    background: var(--page-bg);
    overflow: hidden;
  }
  .hero-photo {
    position: absolute;
    left: 590px;
    top: 0;
    width: 610px;
    height: 800px;
    background:
      radial-gradient(ellipse 45% 35% at 48% 32%, var(--photo-mid) 0%, rgba(44,46,51,0) 100%),
      radial-gradient(ellipse 40% 30% at 60% 70%, rgba(106,81,39,0.55) 0%, rgba(106,81,39,0) 100%),
      radial-gradient(ellipse 30% 25% at 35% 45%, rgba(29,74,99,0.45) 0%, rgba(29,74,99,0) 100%),
      linear-gradient(90deg, var(--page-bg) 0%, var(--photo-deep) 25%, var(--photo-deep) 85%, var(--page-bg) 100%);
  }
  .site-header {
    position: absolute;
    top: 22px;
    left: 250px;
    right: 250px;
    display: flex;
    justify-content: space-between;
    align-items: flex-start;
    z-index: 2;
  }
  .brand {
    display: flex;
    flex-direction: column;
    line-height: 1;
  }
  .brand-name {
    font-weight: 700;
    font-size: 42px;
    letter-spacing: 2px;
    color: var(--text-light);
  }
  .brand-trade {
    font-weight: 400;
    font-size: 13px;
    letter-spacing: 0.5px;
    margin-top: 4px;
  }
  .brand-claim {
    font-weight: 300;
    font-size: 8px;
    color: var(--text-muted);
    margin-top: 3px;
  }
  .main-nav {
    display: flex;
    gap: 8px;
    margin-top: 24px;
    font-size: 11px;
    font-weight: 400;
    letter-spacing: 0.3px;
  }
  .main-nav a {
    color: var(--text-light);
    text-decoration: none;
  }
  .main-nav a.is-active { color: var(--accent-yellow); }
  .main-nav .separator { color: var(--text-muted); }
  .hero-copy {
    position: absolute;
    left: 250px;
    top: 325px;
    z-index: 2;
  }
  .hero-title {
    font-size: 40px;
    line-height: 1.25;
    letter-spacing: -0.5px;
  }
  .hero-title .line-intro {
    display: block;
    font-weight: 300;
    color: var(--accent-cyan);
  }
  .hero-title .word-yellow {
    font-weight: 800;
    color: var(--accent-yellow);
  }
  .hero-title .word-magenta {
    font-weight: 800;
    color: var(--accent-magenta);
  }
  .hero-lead {
    margin-top: 8px;
    font-size: 12.5px;
    font-weight: 500;
    line-height: 1.35;
    letter-spacing: 0.2px;
  }
  .scroll-hint {
    position: absolute;
    left: 598px;
    top: 702px;
    transform: translateX(-50%);
    display: flex;
    flex-direction: column;
    align-items: center;
    gap: 8px;
    z-index: 2;
  }
  .scroll-hint-label {
    font-size: 7px;
    font-weight: 500;
    letter-spacing: 0.5px;
  }
</style>
</head>
<body>
  <main class="hero">
    <div class="hero-photo" role="img" aria-label="Dunkles Porträtfoto mit farbigen Pinselstrichen in Gold, Blau und Rot"></div>

    <header class="site-header">
      <div class="brand">
        <span class="brand-name">LUTZ</span>
        <span class="brand-trade">MALEREIBETRIEB</span>
        <span class="brand-claim">Qualität ist unsere Lieblingsfarbe</span>
      </div>
      <nav class="main-nav">
        <a href="#ueber-uns" class="is-active">ÜBER UNS</a>
        <span class="separator">|</span>
        <a href="#leistungen">LEISTUNGEN</a>
        <span class="separator">|</span>
        <a href="#tipps">WISSENSWERTES &amp; TIPPS</a>
        <span class="separator">|</span>
        <a href="#kontakt">KONTAKT</a>
      </nav>
    </header>

    <section class="hero-copy">
      <h1 class="hero-title">
        <span class="line-intro">Qualität ist</span>
        <span class="word-yellow">Unsere</span> <span class="word-magenta">Lieblingsfarbe</span>
      </h1>
      <p class="hero-lead">PÜNKTLICHKEIT, FREUNDLICHKEIT UND GEWISSENHAFTIGKEIT<br>IN HAMBURG UND UMGEBUNG.</p>
    </section>

    <div class="scroll-hint">
      <span class="scroll-hint-label">SCROLL DOWN</span>
      <svg class="scroll-hint-icon" width="18" height="28" viewBox="0 0 18 28" aria-hidden="true">
        <rect x="1" y="1" width="16" height="26" rx="8" fill="none" stroke="#ffffff" stroke-width="1.6"/>
        <line x1="9" y1="6" x2="9" y2="11" stroke="#ffffff" stroke-width="1.8" stroke-linecap="round"/>
      </svg>
    </div>
  </main>
</body>
</html>
```